Construction Company Needs Letterhead Design

We recently had a new logo designed and would like to have our letterhead updated to a trendier design. We are a concrete construction company based out of Iowa, but do work for Agricultural businesses across the Midwest.

Industry/Entity Type

Construction

Colors
ec1f27
000000
ffffff

Requirements
Must have
• Must stay within our current color scheme of red/black/white. Must have have our address, phone number, e-mail address, etc. printed on the letterhead as well.

```html
<!DOCTYPE html>
<html lang="en">
<head>
<meta charset="utf-8">
<title>Corvane Field Works — Letterhead</title>
<link href="https://fonts.googleapis.com/css2?family=Lato:wght@300;400;700;900&display=swap" rel="stylesheet">
<style>
  :root {
    --brand-red: #ec1f27;
    --brand-black: #0b0b0f;
    --paper: #ffffff;
    --backdrop: #efefef;
    --ink: #3a3a3a;
    --ink-body: #474747;
  }
  * { margin: 0; padding: 0; box-sizing: border-box; }
  html, body {
    width: 1155px; height: 1200px; overflow: hidden;
    background: var(--backdrop);
    font-family: "Lato", Arial, sans-serif;
    color: var(--ink);
  }
  .letterhead {
    position: absolute; left: 157px; top: 32px;
    width: 840px; height: 1135px;
    background: var(--paper);
    box-shadow: 0 6px 18px rgba(0,0,0,0.12);
    overflow: hidden;
  }
  .header-band {
    position: absolute; left: 0; top: 0; width: 100%; height: 34px;
    background: var(--brand-red);
  }
  .header-rule {
    position: absolute; left: 0; top: 40px; width: 100%; height: 5px;
    background: var(--brand-black);
  }
  .brand {
    position: absolute; left: 0; right: 0; top: 80px;
    display: flex; justify-content: center; align-items: center; gap: 12px;
  }
  .brand-mark { width: 34px; height: 34px; background: var(--brand-red); }
  .brand-name {
    font-weight: 900; font-size: 28px; letter-spacing: 0.5px;
    color: var(--brand-black); text-transform: uppercase;
  }
  .letter-date {
    position: absolute; left: 103px; top: 262px;
    font-size: 14.5px; font-weight: 400; color: var(--ink);
  }
  .recipient {
    position: absolute; left: 103px; top: 305px;
    font-size: 13.5px; line-height: 17.6px; font-weight: 400; color: var(--ink);
  }
  .recipient .salutation { font-size: 15px; }
  .letter-body {
    position: absolute; left: 103px; top: 425px; width: 634px;
    font-size: 13.6px; line-height: 22px; font-weight: 400; color: var(--ink-body);
    text-align: justify; hyphens: auto;
  }
  .letter-body p + p { margin-top: 22px; }
  .signature { position: absolute; left: 103px; top: 865px; }
  .signature .signer { font-size: 19px; font-weight: 400; color: var(--ink); }
  .signature .role { font-size: 12.5px; margin-top: 6px; font-weight: 400; color: var(--ink); }
  .footer {
    position: absolute; left: 0; right: 0; top: 1061px;
    text-align: center; font-size: 12.5px; color: var(--ink);
  }
  .footer-contacts {
    margin-top: 6px; display: flex; justify-content: center; gap: 12px;
  }
  .footer-contacts span { display: inline-flex; align-items: center; gap: 5px; }
  .footer-contacts svg { width: 10px; height: 10px; fill: var(--brand-red); }
</style>
</head>
<body>
  <main class="letterhead">
    <div class="header-band"></div>
    <div class="header-rule"></div>

    <div class="brand">
      <div class="brand-mark"></div>
      <div class="brand-name">Corvane Field Works</div>
    </div>

    <div class="letter-date">February 02, 2018</div>

    <div class="recipient">
      <div class="salutation">Dear Mr. Smith,</div>
      <div>demo street,</div>
      <div>demo placeP.O.</div>
      <div>Box 000, 555 Avenue</div>
    </div>

    <div class="letter-body">
      <p>Lorem ipsum dolor sit amet, consectetur adipiscing elit. Donec orci purus, luctus vitae dignissim eu, iaculis sed purus. Vivamus faucibus, ipsum nec aliquet viverra, leo mauris condimentum ligula, sit amet sagittis enim ligula quis arcu. Nam egestas tortor id nisi porttitor mattis. In tortor ante, ultricies in suscipit a, tempus non massa. Vivamus et auctor mi. Fusce vel massa nulla. Phasellus nec eros mauris, et scelerisque orci. Donec malesuada orci vitae nulla accumsan porta a id massa. Quisque accumsan iaculis magna sit amet fringilla. Maecenas consequat, magna eget tincidunt semper, odio nibh rutrum mi, id feugiat ante nisi eu risus. Vestibulum nunc orci, rhoncus a placerat in, ultricies in mi. Cras mattis varius eros, vel fringilla nisi suscipit eget.</p>
      <p>Quisque scelerisque sagittis nulla at porttitor. Mauris a justo et tellus interdum tristique. Sed id augue vitae urna euismod commodo aliquet a quam. Pellentesque arcu velit, cursus et malesuada ut, consequat et diam. Nullam erat sem, rhoncus id ullamcorper vitae, rhoncus et arcu. In ultricies ultricies nulla, ut rutrum nisi iaculis at. Donec eu magna a metus ornare faucibus. Fusce aliquet faucibus ultricies. Morbi semper, est id tincidunt gravida, sem arcu adipiscing lacus, ac bibendum nulla leo eu purus. Quisque nec diam sed risus consectetur a ccumsan quis quis nibh. Vestibulum id purus lorem.</p>
    </div>

    <div class="signature">
      <div class="signer">John Doe</div>
      <div class="role">Co-Founder &amp; CEO</div>
    </div>

    <footer class="footer">
      <div>Demo stree place P.O. Box 000,&nbsp; 555 Avenue, Country</div>
      <div class="footer-contacts">
        <span><svg viewBox="0 0 10 10"><path d="M2 0.5 L4 2.5 L3 3.6 C3.6 5 5 6.4 6.4 7 L7.5 6 L9.5 8 L8 9.5 C4 9 1 6 0.5 2 Z"/></svg>888-8888-8888</span>
        <span><svg viewBox="0 0 10 10"><path d="M0 2 H10 V8 H0 Z M0.8 2.6 L5 5.6 L9.2 2.6 V3.4 L5 6.4 L0.8 3.4 Z" fill-rule="evenodd"/></svg>info@websitename.com</span>
        <span><svg viewBox="0 0 10 10"><path d="M5 0 A5 5 0 1 0 5.01 0 Z M5 1 A4 4 0 1 1 4.99 1 Z M4.5 1 H5.5 V9 H4.5 Z M1 4.5 H9 V5.5 H1 Z" fill-rule="evenodd"/></svg>www.websitename.com</span>
      </div>
    </footer>
  </main>
</body>
</html>
```